Sun Keel (www.sunkeel.com) web site development

Sun Keel is a new Fishing, Spearfishing Charter operator offering private charters in North Belize, Turneffe, Lighthouse Reef and the Blue Hole. The logo of the company has been designed by Pixelvane, some months ago. We have also developed a small brochure which can be the base for the website development (at least colors, fonts, etc.).
Pictures and Video should be an important asset of this website. We need to be able to update contents (video, photos), update prices and destinations, etc.

Target Market(s)

High hand, fishing and spearfishing enthusiasts.

Industry/Entity Type

Yacht charter

Coding

Coded - Design and coding required

Number of Pages Required

4 page

Colors
EB3D1F
EC4F4E
F09395
F8D3D4
FCEDEE

Requirements
Must have
• Optimized for phone and tablet navigation, must be easy to update with photos and video, connected to our Instagram and Facebook page,

```html
<!DOCTYPE html>
<html lang="en">
<head>
<meta charset="utf-8">
<title>Sun Keel – Private Fishing &amp; Spearfishing Charters</title>
<link href="https://fonts.googleapis.com/css2?family=Exo+2:ital,wght@0,700;1,600;1,700;1,800&family=Open+Sans:ital,wght@0,400;0,600;0,700;1,400&display=swap" rel="stylesheet">
<style>
:root{
  --red:#e4222b;
  --teal:#24474d;
  --teal-soft:#5d7b80;
  --ink:#2b3f44;
  --text:#6f7a7d;
  --grey-bg:#ececec;
  --foot-bg:#f3f3f3;
  --white:#ffffff;
  --sea-dark:#1f4a72;
  --sea-mid:#3d78a6;
}
*{box-sizing:border-box;margin:0;padding:0}
html,body{width:1200px;height:4515px;overflow:hidden}
body{position:relative;background:var(--white);font-family:"Open Sans",sans-serif;color:var(--text)}
.abs{position:absolute}
.heading{font-family:"Exo 2",sans-serif;font-style:italic;font-weight:800;color:var(--ink)}
.btn{position:absolute;display:flex;align-items:center;justify-content:center;border-radius:20px;font-family:"Exo 2",sans-serif;font-style:italic;font-weight:700;font-size:12px;letter-spacing:.3px;color:var(--white);text-transform:uppercase}
.btn-red{background:var(--red)}
.btn-teal{background:var(--teal)}
.photo{position:absolute}

/* header */
.site-header{position:absolute;top:0;left:0;width:1200px;height:74px;background:var(--white)}
.brand{position:absolute;display:flex;align-items:center;gap:8px;font-family:"Exo 2",sans-serif;font-style:italic;font-weight:800;color:var(--teal)}
.brand .dot{width:14px;height:14px;border-radius:50%;background:var(--red)}
.main-nav{position:absolute;top:28px;left:390px;display:flex;gap:0}
.main-nav a{position:absolute;white-space:nowrap;font-family:"Exo 2",sans-serif;font-style:italic;font-weight:700;font-size:12px;color:var(--ink);text-decoration:none;letter-spacing:.4px}
.main-nav a.active{color:var(--red)}

/* hero */
.hero-title{position:absolute;top:160px;left:0;width:1200px;text-align:center;font-size:44px;color:var(--white)}
.service-circle{position:absolute;width:298px;height:298px;border-radius:50%;border:7px solid var(--teal-soft);overflow:hidden}
.service-circle.featured{border-color:var(--red)}
.service-circle span{position:absolute;left:0;width:100%;text-align:center;font-family:"Exo 2",sans-serif;font-style:italic;font-weight:700;font-size:16px;color:var(--white);line-height:18px}

/* welcome */
.section-title{position:absolute;left:0;width:1200px;text-align:center;font-size:34px}
.lead{position:absolute;text-align:center;font-size:11.5px;line-height:19px;color:var(--text)}

/* machine */
.machine{position:absolute;top:1007px;left:0;width:1200px;height:438px;background:var(--teal)}
.specs{position:absolute;left:200px;top:143px;font-family:"Exo 2",sans-serif;font-style:italic;font-weight:700;font-size:16px;line-height:25px;color:var(--white)}
.specs .model{color:var(--red)}

/* charters */
.card{position:absolute;top:1659px;width:250px;height:492px;background:#f8f8f8;box-shadow:0 6px 18px rgba(0,0,0,.08)}
.card .thumb{position:absolute;top:0;left:0;width:250px;height:186px}
.card .price{position:absolute;top:164px;left:0;height:22px;padding:0 14px 0 18px;background:var(--red);color:var(--white);font-family:"Exo 2",sans-serif;font-style:italic;font-weight:700;font-size:11px;line-height:22px}
.card h3{position:absolute;top:204px;left:18px;font-family:"Exo 2",sans-serif;font-style:italic;font-weight:800;font-size:13px;line-height:15px;color:var(--ink);text-transform:uppercase}
.card p{position:absolute;left:18px;width:218px;font-size:9.2px;line-height:14.6px;color:var(--text)}
.card p b{color:var(--ink);font-weight:700}
.card .btn{top:435px;left:18px;width:125px;height:36px}

/* includes */
.inc{position:absolute;top:2272px;width:133px;height:132px;text-align:center}
.inc.divider{border-right:1px solid #d7d7d7}
.inc.highlight{background:var(--white);box-shadow:0 4px 16px rgba(0,0,0,.12)}
.inc svg{position:absolute;top:28px;left:46px}
.inc span{position:absolute;top:82px;left:0;width:133px;font-family:"Exo 2",sans-serif;font-style:italic;font-weight:700;font-size:13px;color:var(--ink)}
.inc.highlight span{color:var(--red);text-decoration:underline}

/* why us */
.why{position:absolute;top:2467px;left:0;width:1200px;height:436px;background:var(--red)}
.why p{position:absolute;left:200px;top:120px;width:335px;font-size:13.5px;line-height:22.5px;color:var(--white)}

/* testimonial */
.quote{position:absolute;top:3130px;left:290px;width:620px;text-align:center;font-style:italic;font-size:11px;line-height:19px;color:var(--text)}

/* gallery */
.tabs{position:absolute;top:3541px;left:488px;width:224px;height:24px;border:1px solid var(--teal);border-radius:12px;overflow:hidden;display:flex}
.tabs span{flex:1;text-align:center;font-size:11px;font-weight:700;line-height:22px;color:var(--ink)}
.tabs span.on{background:var(--teal);color:var(--white)}

/* footer */
.footer-col h4{font-family:"Exo 2",sans-serif;font-style:italic;font-weight:700;font-size:16px;color:var(--ink);margin-bottom:14px}
.footer-col{position:absolute;top:4260px;font-size:11px;line-height:20px;color:var(--text)}
.footer-col a{display:block;color:var(--text);text-decoration:none;font-size:10.5px;line-height:22px}
.side-tab{position:absolute;left:1072px;top:3998px;width:54px;height:168px;border-radius:27px;background:var(--teal)}
.side-tab .ring{position:absolute;top:0;left:0;width:54px;height:54px;border-radius:50%;background:var(--white);border:3px solid var(--teal);display:flex;align-items:center;justify-content:center;font-family:"Exo 2",sans-serif;font-style:italic;font-weight:800;font-size:9px;color:var(--teal)}
.side-tab .vlabel{position:absolute;left:27px;top:112px;transform:translate(-50%,-50%) rotate(-90deg);white-space:nowrap;font-family:"Exo 2",sans-serif;font-style:italic;font-weight:700;font-size:11px;color:var(--white)}
</style>
</head>
<body>

<!-- Header -->
<header class="site-header">
  <div class="brand" style="left:200px;top:22px;font-size:24px"><span class="dot"></span>Sun Keel</div>
  <nav class="main-nav">
    <a class="active" href="#" style="left:0">HOME</a>
    <a href="#" style="left:62px">ABOUT US</a>
    <a href="#" style="left:150px">PRIVATE CHARTERS</a>
    <a href="#" style="left:297px">GALLERY</a>
    <a href="#" style="left:376px">CONTACT US</a>
  </nav>
  <div class="btn btn-teal" style="left:874px;top:19px;width:125px;height:37px;">Book Now!</div>
</header>

<!-- Hero -->
<section class="hero">
  <div class="photo" role="img" aria-label="Anglers fighting a fish from the back of a boat on deep blue sea" style="top:74px;left:0;width:1200px;height:560px;background:linear-gradient(160deg,#16385c 0%,#2c5f8c 45%,#3f6f8e 70%,#6b8a97 100%)"></div>
  <h1 class="hero-title heading">Just Bring Appetite for Adventure</h1>
  <div class="btn btn-red" style="left:500px;top:238px;width:197px;height:34px">Book Your Trip Today!</div>
  <svg class="abs" style="top:450px;left:0" width="1200" height="240" viewBox="0 0 1200 240">
    <path d="M0,72 C300,190 800,178 1200,20 L1200,42 C800,195 300,205 0,94 Z" fill="var(--red)"/>
    <path d="M0,94 C300,205 800,195 1200,42 L1200,240 L0,240 Z" fill="var(--white)"/>
  </svg>
  <div class="service-circle" style="left:214px;top:377px">
    <div class="photo" role="img" aria-label="Angler holding up a large caught fish" style="inset:0;background:linear-gradient(180deg,#7fa3c4 0%,#567a92 55%,#34505c 100%)"></div>
    <span style="top:214px">Fishing</span>
  </div>
  <div class="service-circle featured" style="left:456px;top:377px">
    <div class="photo" role="img" aria-label="Spearfisher underwater in clear turquoise water" style="inset:0;background:linear-gradient(180deg,#3fa5b4 0%,#2c7f8e 55%,#1f5b66 100%)"></div>
    <span style="top:214px">Spearfishing</span>
  </div>
  <div class="service-circle" style="left:701px;top:377px">
    <div class="photo" role="img" aria-label="Private charter boat cruising on open water" style="inset:0;background:linear-gradient(180deg,#5b85a8 0%,#45708f 55%,#2f5670 100%)"></div>
    <span style="top:205px">Snorkelling Private<br>Charters</span>
  </div>
</section>

<!-- Welcome -->
<section class="welcome">
  <h2 class="section-title heading" style="top:725px">Welcome to <span style="color:var(--red)">Sun Keel</span></h2>
  <p class="lead" style="top:787px;left:263px;width:674px">Sun Keel offers Fishing, Spearfishing and Snorkeling private charters in North Belize, Turneffe, Lighthouse Reef and the Blue Hole. No need to board crowded boats. Choose your privacy and let us pamper you with our exclusive service. Whether it is Snorkelling for the family, Tuna for the experienced angler, or Deep Sea Spearfishing for the fight of a lifetime, you will surely be pleased. Not only do we offer a vast assortment of trips but our local guides will coach you through each fight to ensure you catch your desired Trophy Fish.</p>
  <div class="btn btn-red" style="left:538px;top:909px;width:124px;height:33px">Read More</div>
</section>

<!-- Fishing machine -->
<section class="machine">
  <svg class="abs" style="top:0;left:0" width="1200" height="438" viewBox="0 0 1200 438">
    <path role="img" aria-label="Sport fishing yacht moored near a green shoreline" d="M628,0 C540,110 700,300 600,438 L1200,438 L1200,0 Z" fill="url(#yachtSky)"/>
    <defs>
      <linearGradient id="yachtSky" x1="0" y1="0" x2="0" y2="1">
        <stop offset="0" stop-color="#8fb6d8"/>
        <stop offset=".55" stop-color="#c7d8e2"/>
        <stop offset=".75" stop-color="#6b8c6a"/>
        <stop offset="1" stop-color="#3f6f8a"/>
      </linearGradient>
    </defs>
    <path d="M628,0 C540,110 700,300 600,438" fill="none" stroke="var(--red)" stroke-width="18"/>
  </svg>
  <h2 class="heading abs" style="left:200px;top:58px;font-size:32px;line-height:34px;color:var(--white)">OUR FISHING<br>MACHINE</h2>
  <div class="specs">
    <div class="model">Halvern 290 Open</div>
    <div>LFT: 31'10" ; Beam: 11'6"</div>
    <div>Draft.: 2'0" ; Weight.10,000</div>
    <div>Fuel: 302 gals.</div>
    <div>Water: 55 gals.</div>
    <div>Engines: 2 x 350hp Inboard</div>
    <div>Cruise Speed: 20kn</div>
  </div>
  <div class="btn btn-red" style="left:200px;top:337px;width:241px;height:35px">Call and Book Your Trip Today!</div>
</section>

<!-- Our charters -->
<section class="charters">
  <h2 class="section-title heading" style="top:1497px">Our Charters</h2>
  <p class="lead" style="top:1557px;left:263px;width:674px">We welcome both experienced fishermen/free divers and beginners. You can learn from our guides and even attend one of our introductory class to free dive and spearfishing from professional licensed instructors and expert scuba divers. You are welcome to take your gear with you, or leave us to provide you with all you need for an unforgettable experience. What you need to take with you is just your appetite for adventure.</p>

  <article class="card" style="left:200px">
    <div class="thumb" role="img" aria-label="Angler on deck with a large tuna under a cloudy sky" style="background:linear-gradient(180deg,#6f9fcf 0%,#9dbcd6 50%,#4a6f86 100%)"></div>
    <div class="price">US$1.000</div>
    <h3>Fishing Private<br>Charters</h3>
    <p style="top:250px">Our Fishing Charters are all Offshore Trips. Depending on your choice we can offer a variety of fishing options. For the experienced angler, test your skills by casting lures or if you're just a beginner bottom fishing baits is always a good way to go. We specialise in putting you on big fish and will do what it takes to make sure you get a chance to experience what drag screaming is all about.<br><b>Maximum 6 guests (4 anglers).</b></p>
    <div class="btn btn-teal">Book Now</div>
  </article>

  <article class="card" style="left:475px">
    <div class="thumb" role="img" aria-label="Diver underwater holding a large green fish" style="background:linear-gradient(180deg,#1b6fb0 0%,#1a5a95 60%,#123e6c 100%)"></div>
    <div class="price">US$1.400</div>
    <h3>Spearfishing Private<br>Charters</h3>
    <p style="top:250px">We welcome all experience levels and you will be accompanied by a safe diver in the water at all times to help you with anything you need! You are welcome to take along your equipment, however we provide the best equipment in the market.<br><br>Our fishing grounds are all offshore so our Spearfishing Charters are all full day <b>(minimum 8 hours). Maximum of 6 guests (4 divers)</b></p>
    <div class="btn btn-red">Book Now</div>
  </article>

  <article class="card" style="left:750px">
    <div class="thumb" role="img" aria-label="Group of snorkelers swimming among a school of fish" style="background:linear-gradient(180deg,#5fb4d4 0%,#4c97b8 55%,#3a7795 100%)"></div>
    <div class="price">US$1.200</div>
    <h3>Snorkelling Private<br>Charters</h3>
    <p style="top:250px">We offer snorkelling trips to the Hole Chan Marine Reserve, to Shark Ray Alley, Coral Gardens, all destinations inside the barrier reef and in calm waters. But we also offer snorkelling trips to the offshore Atolls: Turneffe North or South, Half Moon Caye National Park and the Blue Hole.<br><br><b>Our Snorkelling Trips are full day (minimum 8 hours). Maximum 6 guests.</b></p>
    <div class="btn btn-teal">Book Now</div>
  </article>
</section>

<!-- Includes -->
<section class="includes">
  <h2 class="section-title heading" style="top:2205px">Our Charters Includes</h2>
  <div class="inc divider" style="left:200px">
    <svg width="40" height="40" viewBox="0 0 40 40" fill="none" stroke="var(--teal)" stroke-width="2.5" stroke-linecap="round"><path d="M6,36 L34,4"/><path d="M34,4 L34,26"/><circle cx="12" cy="29" r="4"/><path d="M34,26 q-3,4 -6,0"/></svg>
    <span>Equipments</span>
  </div>
  <div class="inc divider" style="left:333px">
    <svg width="40" height="40" viewBox="0 0 40 40" fill="none" stroke="var(--teal)" stroke-width="2.5" stroke-linejoin="round"><rect x="7" y="8" width="18" height="26" rx="2"/><rect x="11" y="13" width="10" height="7" fill="var(--teal)"/><path d="M25,14 h5 v14 a3,3 0 0 0 6,0 v-16 l-4,-4"/></svg>
    <span>fuel</span>
  </div>
  <div class="inc highlight" style="left:466px">
    <svg width="40" height="40" viewBox="0 0 40 40" fill="var(--red)"><path d="M8,14 q12,-12 24,0 v3 h-24 z"/><rect x="11" y="19" width="18" height="10" rx="5"/><path d="M6,38 q2,-8 14,-8 q12,0 14,8 z"/></svg>
    <span>Captain</span>
  </div>
  <div class="inc divider" style="left:599px">
    <svg width="40" height="40" viewBox="0 0 40 40" fill="var(--teal)"><circle cx="16" cy="10" r="6"/><path d="M5,38 q1,-17 11,-17 q10,0 11,17 z"/><path d="M28,10 v28" stroke="var(--teal)" stroke-width="2.5"/><path d="M28,10 l9,4 l-9,4 z"/></svg>
    <span>Guide</span>
  </div>
  <div class="inc divider" style="left:732px">
    <svg width="40" height="40" viewBox="0 0 40 40" fill="none" stroke="var(--teal)" stroke-width="2.5" stroke-linejoin="round"><path d="M6,8 h24 l-12,14 z" fill="var(--teal)"/><path d="M18,22 v12 M11,35 h14"/><circle cx="31" cy="8" r="5"/></svg>
    <span>Drinks (soft)</span>
  </div>
  <div class="inc" style="left:865px">
    <svg width="40" height="40" viewBox="0 0 40 40" fill="none" stroke="var(--teal)" stroke-width="2.5" stroke-linecap="round"><path d="M12,4 v10 M8,4 v6 q0,4 4,4 q4,0 4,-4 v-6 M12,14 v10"/><path d="M28,4 q-5,4 -4,12 h4 v8"/><path d="M4,28 h32 q-2,8 -16,8 q-14,0 -16,-8 z" fill="var(--teal)"/></svg>
    <span>lunch</span>
  </div>
</section>

<!-- Why us -->
<section class="why">
  <svg class="abs" style="top:0;left:0" width="1200" height="436" viewBox="0 0 1200 436">
    <defs>
      <linearGradient id="whySea" x1="0" y1="0" x2="0" y2="1">
        <stop offset="0" stop-color="#2a5f96"/>
        <stop offset=".5" stop-color="#1f4f86"/>
        <stop offset="1" stop-color="#173c6a"/>
      </linearGradient>
    </defs>
    <path role="img" aria-label="Cruising yacht speeding across deep blue water" d="M600,0 C520,110 700,300 610,436 L1200,436 L1200,0 Z" fill="url(#whySea)"/>
    <path d="M600,0 C520,110 700,300 610,436" fill="none" stroke="var(--teal)" stroke-width="16"/>
  </svg>
  <h2 class="heading abs" style="left:200px;top:60px;font-size:32px;color:var(--white)">Why US</h2>
  <p>Sun Keel, our boat is the largest open fishing boat in North Belize. The only one offering not only large space on board, but also large space shaded from sun and from the elements. A boat ment for offshore navigation and the only one that can take guest in safe and comfort to cruise towards the offshore atolls. Last but not least the only one offering a real toilet with shower.</p>
  <div class="btn btn-teal" style="left:200px;top:328px;width:198px;height:34px">Book Your Trip Today!</div>
</section>

<!-- Testimonials -->
<section class="testimonials">
  <h2 class="section-title heading" style="top:2955px">What Our Guests Say</h2>
  <div class="abs" style="left:563px;top:3022px;width:74px;height:74px;border-radius:50%;border:2px solid var(--red);padding:4px;background:var(--white)">
    <div role="img" aria-label="Guest portrait" style="width:100%;height:100%;border-radius:50%;background:linear-gradient(180deg,#9fc3dc,#4d7a95)"></div>
  </div>
  <div class="abs" style="top:3104px;left:0;width:1200px;text-align:center;color:var(--red);font-size:12px;letter-spacing:1px">★★★★★</div>
  <svg class="abs" style="left:198px;top:3158px" width="14" height="24" viewBox="0 0 14 24"><path d="M12,2 L3,12 L12,22" fill="none" stroke="var(--ink)" stroke-width="2"/></svg>
  <svg class="abs" style="left:988px;top:3158px" width="14" height="24" viewBox="0 0 14 24"><path d="M2,2 L11,12 L2,22" fill="none" stroke="var(--ink)" stroke-width="2"/></svg>
  <p class="quote">There are many variations of passages of Lorem Ipsum available, but the majority have suffered alteration in some form, by injected humour, or randomised words which don't look even slightly believable. If you are going to use a passage of Lorem Ipsum, you need to be sure there isn't anything embarrassing hidden in the middle of text. All the Lorem Ipsum generators on the Internet tend to repeat predefined chunks as necessary, making this the first true generator on the Internet. It uses a dictionary of over 200 Latin words, combined with a handful of model sentence</p>
  <div class="abs" style="top:3255px;left:0;width:1200px;text-align:center;font-family:'Exo 2',sans-serif;font-style:italic;font-weight:700;font-size:12px;color:var(--ink)">Standard Chunk</div>
</section>

<!-- Gallery -->
<section class="gallery">
  <svg class="abs" style="top:3300px;left:0" width="1200" height="160" viewBox="0 0 1200 160">
    <path d="M0,118 C300,170 700,30 1200,2 L1200,18 C700,46 300,186 0,134 Z" fill="var(--red)"/>
    <path d="M0,134 C300,186 700,46 1200,18 L1200,26 C700,54 300,194 0,142 Z" fill="var(--teal)"/>
    <path d="M0,142 C300,194 700,54 1200,26 L1200,160 L0,160 Z" fill="var(--grey-bg)"/>
  </svg>
  <div class="abs" style="top:3460px;left:0;width:1200px;height:640px;background:var(--grey-bg)"></div>
  <h2 class="section-title heading" style="top:3460px">Gallery</h2>
  <div class="abs" style="top:3553px;left:295px;width:610px;height:1px;background:#bdbdbd"></div>
  <div class="tabs"><span class="on">Photos</span><span style="background:var(--white)">Video</span></div>
  <div class="photo" role="img" aria-label="Angler reeling in from the bow of a sailboat" style="left:200px;top:3583px;width:387px;height:336px;background:linear-gradient(180deg,#9bb4c9 0%,#7b9ab5 45%,#2b5c8c 100%)"></div>
  <div class="photo" role="img" aria-label="Anglers on a boat deck with rods out at sea" style="left:611px;top:3583px;width:389px;height:154px;background:linear-gradient(180deg,#7ea6cf 0%,#2f6aa6 50%,#203f5e 100%)"></div>
  <div class="photo" role="img" aria-label="Diver above a coral reef in blue water" style="left:611px;top:3763px;width:182px;height:156px;background:linear-gradient(180deg,#3aa0d8 0%,#2a7fb8 60%,#1e5f8c 100%)"></div>
  <div class="photo" role="img" aria-label="Spearfisher underwater in green-blue water" style="left:818px;top:3763px;width:182px;height:156px;background:linear-gradient(180deg,#4bb4b0 0%,#2f8a88 60%,#1f5c60 100%)"></div>
  <div class="btn btn-red" style="left:538px;top:3954px;width:124px;height:33px">View All</div>
</section>

<!-- Footer -->
<footer class="site-footer">
  <svg class="abs" style="top:4040px;left:0" width="1200" height="120" viewBox="0 0 1200 120">
    <path d="M0,0 L1200,0 L1200,10 C800,-10 400,150 0,66 Z" fill="var(--grey-bg)"/>
    <path d="M0,66 C400,150 800,-10 1200,10 L1200,26 C800,6 400,166 0,82 Z" fill="var(--red)"/>
    <path d="M0,82 C400,166 800,6 1200,26 L1200,32 C800,12 400,172 0,88 Z" fill="var(--teal)"/>
    <path d="M0,88 C400,172 800,12 1200,32 L1200,120 L0,120 Z" fill="var(--foot-bg)"/>
  </svg>
  <div class="abs" style="top:4160px;left:0;width:1200px;height:355px;background:var(--foot-bg)"></div>

  <div class="side-tab"><div class="ring">Sun Keel</div><div class="vlabel">CONTACT US</div></div>

  <div class="brand" style="left:200px;top:4292px;font-size:38px"><span class="dot" style="width:22px;height:22px"></span>Sun Keel</div>

  <div class="footer-col" style="left:405px;width:210px">
    <h4>Contact Us</h4>
    <div style="font-size:14px;line-height:20px;color:var(--ink)">Call Us: 6104217</div>
    <div style="font-size:10.5px">e. info@sunkeel.com</div>
    <div style="margin-top:22px;font-size:10px;line-height:14px"><b style="color:var(--ink)">Address:</b><br>Palm Row Guesthouse, Calle Marea,<br>Caye Caulker</div>
  </div>
  <div class="footer-col" style="left:667px;width:130px">
    <h4>Quick Links</h4>
    <a href="#">Home</a>
    <a href="#">About Us</a>
    <a href="#">Private Charters</a>
    <a href="#">Gallery</a>
    <a href="#">Contact Us</a>
  </div>
  <div class="footer-col" style="left:818px;width:182px">
    <h4>Sign Up Newsletter</h4>
    <div style="font-size:9.5px;line-height:14px">There are many variations of passages lorem ipsum available</div>
    <div style="margin-top:14px;height:24px;border-radius:12px;background:var(--teal);color:#c9d4d6;font-size:9px;line-height:24px;padding-left:12px">Enter your email ...</div>
    <div style="margin-top:8px;width:88px;height:24px;border-radius:12px;background:var(--red);color:var(--white);text-align:center;font-family:'Exo 2',sans-serif;font-style:italic;font-weight:700;font-size:10px;line-height:24px">SEND</div>
  </div>

  <div class="abs" style="top:4445px;left:200px;width:800px;height:1px;background:#cfcfcf"></div>
  <div class="abs" style="top:4469px;left:200px;font-size:10px;color:var(--text)">© 2021 <b style="color:var(--ink)">Sun Keel</b> All Right Reserved</div>
  <div class="abs" style="top:4464px;left:820px;width:22px;height:22px;border-radius:50%;background:var(--teal)"></div>
  <div class="abs" style="top:4464px;left:851px;width:22px;height:22px;border-radius:50%;background:var(--teal)"></div>
</footer>

</body>
</html>
```